Artificial intelligence, machine learning, and automation company needs a sexy business card design

We need a sleek and sexy business card design for an AI consulting company based in Philadelphia PA. We provide custom machine learning and automation solutions for companies of all shapes and sizes. The primary industries that we serve are pharmaceuticals, engineering, healthcare, and computer software. We would like the designs to be a black business card that uses green as a sleek accent color. The final design should communicate intelligence, cutting edge new-tech, and optimization.

Target Market(s)

C-level and VP level executives of multi-million annual companies. Mostly in Pharma, Healthcare, Real Estate, Retail, and Engineering

Industry/Entity Type

Computer Software

Contact Information for Business Card

Name: Jed Harlow
Title: CEO
Cell: 484 562 0937
Email: JedH@quillorbit.example
Website: www.QuillOrbit.example

Font styles to use
Sans Serif

Colors

Designer to choose colors to be used in the design.

Requirements
Must have
• 1) Attached Quillon Logo (either with colors or not/embossed)
• 2) "Artificial Intelligence" "Automation" and "Machine Learning"
• 3) "Quillon Laboratories" or "Quillon Labs" or "Quillon"
• 4) Sexy AF.
Nice to have
• Black card / dark card color, "Quillon Green" accent colors (in attached .ai file), Embossment of logo/name/etc, thick card stock, colored borders (on card sides, not front/back faces)
Should not have
• Should not be bland, or unsexy.

```html
<!DOCTYPE html>
<html lang="en">
<head>
<meta charset="utf-8">
<title>Quillon Laboratories — Business Card</title>
<link rel="stylesheet" href="https://fonts.googleapis.com/css2?family=Montserrat:wght@400;500&family=Oswald:wght@500&family=Open+Sans:wght@400&display=swap">
<style>
  :root {
    --backdrop: #d9d6d2;
    --card-dark: #232323;
    --card-light: #2f2f2f;
    --quillon-green: #3ec9b0;
    --ink-light: #f2f2f2;
    --ink-muted: #c9c9c9;
  }
  * { margin: 0; padding: 0; box-sizing: border-box; }
  html, body {
    width: 1200px; height: 715px; overflow: hidden;
    background: var(--backdrop);
  }
  .sheet {
    position: relative; width: 1200px; height: 715px;
    display: flex; align-items: center; justify-content: center; gap: 40px;
  }
  .card {
    position: relative; width: 540px; height: 309px; overflow: hidden;
    box-shadow: 0 14px 30px rgba(0,0,0,.35);
  }
  .card__texture {
    position: absolute; inset: 0;
    background: linear-gradient(135deg, var(--card-light) 0%, var(--card-dark) 45%, #2b2b2b 70%, var(--card-dark) 100%);
  }
  /* Front */
  .brand {
    position: absolute; left: 92px; top: 96px;
    display: flex; align-items: center; gap: 16px;
  }
  .brand__mark {
    width: 52px; height: 52px; border: 3px solid var(--quillon-green);
  }
  .brand__name {
    font-family: "Montserrat", sans-serif; font-weight: 400; color: var(--ink-light);
    line-height: 1;
  }
  .brand__word {
    display: block; font-size: 40px; letter-spacing: 9px;
  }
  .brand__sub {
    display: block; font-size: 17px; letter-spacing: 6.4px; margin-top: 6px;
  }
  .tagline {
    position: absolute; left: 92px; top: 196px;
    font-family: "Montserrat", sans-serif; font-weight: 400; font-size: 13.5px;
    color: var(--ink-muted); letter-spacing: .2px;
  }
  /* Back */
  .rule {
    position: absolute; left: 48px; width: 3px; background: var(--quillon-green);
  }
  .rule--top { top: 0; height: 46px; }
  .rule--mid { top: 98px; height: 112px; }
  .rule--low { top: 270px; height: 39px; }
  .person {
    position: absolute; left: 48px; top: 52px;
  }
  .person__name {
    font-family: "Oswald", sans-serif; font-weight: 500; font-size: 22px;
    color: var(--quillon-green); letter-spacing: .5px; text-transform: uppercase;
    padding-left: 8px;
  }
  .person__title {
    font-family: "Open Sans", sans-serif; font-size: 11px; color: var(--ink-muted);
    margin-top: 0;
  }
  .contact {
    position: absolute; left: 28px; top: 216px; list-style: none;
    font-family: "Open Sans", sans-serif; color: var(--ink-light); font-size: 14px;
  }
  .contact__item { display: flex; align-items: center; gap: 10px; height: 20px; }
  .contact__icon { width: 12px; height: 12px; fill: var(--ink-light); }
  .contact__web {
    font-size: 17px; color: var(--quillon-green); margin-top: 3px; letter-spacing: .3px;
  }
</style>
</head>
<body>
<main class="sheet">
  <section class="card card--front">
    <div class="card__texture" role="img" aria-label="Dark low-poly faceted texture"></div>
    <div class="brand">
      <span class="brand__mark"></span>
      <span class="brand__name">
        <span class="brand__word">QUILLON</span>
        <span class="brand__sub">LABORATORIES</span>
      </span>
    </div>
    <p class="tagline">Artificial Intelligence, Automation and Machine Learning</p>
  </section>

  <section class="card card--back">
    <div class="card__texture" role="img" aria-label="Dark low-poly faceted texture"></div>
    <span class="rule rule--top"></span>
    <span class="rule rule--mid"></span>
    <span class="rule rule--low"></span>
    <div class="person">
      <p class="person__name">Jed Harlow</p>
      <p class="person__title">CEO</p>
    </div>
    <ul class="contact">
      <li class="contact__item">
        <svg class="contact__icon" viewBox="0 0 12 12" aria-hidden="true"><path d="M2.5 1h2l1 2.5-1.3 1a6 6 0 0 0 2.8 2.8l1-1.3 2.5 1v2a1 1 0 0 1-1 1A9 9 0 0 1 1.5 2a1 1 0 0 1 1-1z"/></svg>
        <span>484 562 0937</span>
      </li>
      <li class="contact__item">
        <svg class="contact__icon" viewBox="0 0 12 12" aria-hidden="true"><path d="M1 2.5h10v7H1z M1.6 3l4.4 3.4L10.4 3" fill="none" stroke="#f2f2f2" stroke-width="1"/></svg>
        <span>JedH@quillorbit.example</span>
      </li>
      <li class="contact__web">www.QuillOrbit.example</li>
    </ul>
  </section>
</main>
</body>
</html>
```